WP website design (Stoneridge)

We need a wordpress design that will incorporate a professional color scheme with company logo in a clean layout. The design needs to consider that this will be developed on a responsive theme. Colors are either 1) green of the logo, and tan and an accent color maybe black; or other highlight for the logo that without the green. Client wants a 'modern' look.

Industry/Entity Type

It Company

Number of Pages Required

1 page

Font styles to use
Serif
Sans Serif

Requirements
Must have
• Navigation - 1) Home 2) Real Estate 3) Auction Calendar 4) About Us 5) Terms & Conditions 6) FAQ 7) Contact Us
• Site will have full width slideshow 960px. Use stock real estate photo. Header will have logo (attached) and contact info:
• Main Office:
• 417 E Hazel Rd
• Marston, VA 24873
• (800) 555-0173
• (540) 555-0148
• Dunmore Office:
• 318 1/2 S. Mill Rd.
• Dunmore, WV 24987
• (304) 555-0161
• Widgets - in the sidebar or footer of site - email signup form; featured auctions; testimonials; Facebook and RSS social icons; link to broker participation form; News and Events Blog.
Nice to have
• use of dropdown menus styling displayed - 1) Current Auctions & 2) Past Auctions under the Auction Calendar link

```html
<!DOCTYPE html>
<html lang="en">
<head>
<meta charset="utf-8">
<title>Stoneridge Real Estate &amp; Auction</title>
<link rel="stylesheet" href="https://fonts.googleapis.com/css2?family=Marcellus&family=Open+Sans:wght@400;600;700&family=PT+Sans:wght@400;700&display=swap">
<style>
:root{
  --dark:#231f1e;
  --gold:#f6c04e;
  --gold-soft:#f9d27f;
  --gold-text:#e9b24a;
  --ink:#222;
  --white:#fff;
  --panel:#f4f4f4;
  --line:#d9d9d9;
  --pin:#d0121b;
}
*{margin:0;padding:0;box-sizing:border-box}
html,body{width:854px;height:1200px;overflow:hidden;background:var(--dark);font-family:"Open Sans",sans-serif;color:var(--ink)}
.canvas{position:relative;width:854px;height:1200px}
.page{position:absolute;left:90px;top:0;width:676px;height:1011px;background:var(--white)}
.abs{position:absolute}
.brand{display:flex;align-items:center;gap:8px}
.brand-dot{border-radius:50%;background:var(--gold);flex:none}
.brand-name{font-family:"Marcellus",serif;color:var(--dark)}
.header-brand{left:14px;top:28px}
.header-brand .brand-dot{width:26px;height:26px}
.header-brand .brand-name{font-size:26px}
.offices{left:236px;top:22px;display:flex;gap:26px;font-size:8.5px;line-height:11.5px;color:var(--ink);white-space:nowrap}
.offices b{font-weight:700;color:var(--dark)}
.social{left:577px;top:33px;display:flex;gap:8px}
.social span{width:24px;height:24px;border-radius:50%;background:#cfd6dd;border:2px solid #e8ecef}
.nav{left:0;top:88px;width:676px;height:32px;background:var(--gold);display:flex;align-items:center;justify-content:space-between;padding:0 14px;font-family:"PT Sans",sans-serif;font-weight:700;font-size:11px;color:var(--dark);white-space:nowrap}
.nav a{flex:1;text-align:center;height:20px;line-height:20px;border-right:1px solid #b9852a;text-decoration:none;color:inherit}
.nav a:last-child{border:none}
.nav a.wide{flex:1.6}
.dropdown{left:193px;top:120px;width:130px;font-family:"Open Sans",sans-serif;font-size:10px}
.dropdown div{height:24px;line-height:24px;padding-left:15px}
.dropdown .d1{background:var(--gold-soft);color:var(--white)}
.dropdown .d2{background:var(--dark);color:var(--white)}
.slider{left:16px;top:144px;width:418px;height:168px;background:linear-gradient(180deg,#7e98b3 0%,#c9c4b8 45%,#8b7e6c 80%,#5b5a43 100%)}
.dots{left:206px;top:292px;display:flex;gap:8px}
.dots span{width:10px;height:10px;border-radius:50%;background:var(--white)}
.dots span.on{background:#d9a83a}
.signup{left:457px;top:143px;width:209px;height:170px;background:var(--gold);padding:0 23px}
.signup h3{font-family:"Marcellus",serif;font-weight:400;font-size:21px;color:var(--dark);margin-top:14px}
.signup p{font-size:9px;color:var(--white);line-height:13px;margin-top:8px}
.signup .field{margin-top:8px;width:161px;height:24px;background:var(--white);font-size:9px;color:#666;padding-left:8px;line-height:24px}
.signup .btn{margin-top:16px;display:inline-block;background:var(--dark);color:var(--white);font-family:"PT Sans",sans-serif;font-weight:700;font-size:11px;padding:4px 12px;border:1px solid #000}
.welcome{left:13px;top:356px;width:420px}
.welcome h1{font-family:"Marcellus",serif;font-weight:400;font-size:20px}
.welcome p{font-size:9px;line-height:14.5px;margin-top:9px;padding-left:4px}
.listing{left:14px;width:412px;border:1px solid var(--line);background:var(--panel)}
.listing h2{background:var(--gold);height:29px;line-height:30px;padding-left:11px;font-family:"Marcellus",serif;font-weight:400;font-size:13px;color:var(--white);letter-spacing:.3px}
.listing .body{position:relative;height:175px}
.listing .photo{position:absolute;left:12px;top:14px;width:178px;height:113px;background:linear-gradient(180deg,#c9d4dc 0%,#9a978f 50%,#5b7a3c 100%);box-shadow:1px 1px 3px rgba(0,0,0,.3)}
.listing .btns{position:absolute;left:21px;top:143px;display:flex;gap:20px}
.listing .btns span{width:68px;height:22px;background:var(--dark);color:var(--white);font-size:9px;line-height:22px;display:flex;align-items:center;gap:6px;padding-left:9px;border-radius:2px}
.listing .btns i{width:11px;height:9px;background:#9fb3cc;display:block}
.listing .info{position:absolute;left:210px;top:19px;width:196px;font-family:"PT Sans",sans-serif;font-size:8.5px;line-height:12.7px;letter-spacing:.2px}
.listing .info h4{font-size:11.5px;font-weight:700;line-height:15px;margin-bottom:5px;width:160px}
.listing .info .sell{width:196px}
.listing .info b{font-weight:700}
.pinrow{display:flex;align-items:center;gap:3px;white-space:nowrap}
.video{left:458px;top:361px;width:206px;height:147px;background:linear-gradient(180deg,#d9d6cf 0%,#6d6a55 60%,#3a3a2c 100%)}
.play{left:83px;top:38px;width:48px;height:48px;border-radius:50%;background:rgba(30,30,30,.8)}
.vbar{left:0;bottom:0;width:206px;height:10px;background:#1a1a1a}
.vtrack{left:18px;top:3px;width:80px;height:3px;background:#777}
.widget{left:458px;width:206px;border:1px solid var(--line);background:var(--panel);padding:0 14px}
.widget h3{font-family:"Marcellus",serif;font-weight:400;font-size:19px;color:var(--gold-text);margin-top:14px}
.featured{top:530px;height:217px;text-align:center;font-size:8px;line-height:11px}
.featured .t{font-weight:600;margin-top:14px}
.featured .img{width:118px;height:71px;margin:7px auto 0;border:2px solid #c9a55b;background:linear-gradient(180deg,#b7c5c9 0%,#8d9077 55%,#5e7a45 100%)}
.featured .b{margin-top:15px}
.news{top:772px;height:192px}
.news ul{list-style:none;margin-top:14px;font-size:8px;line-height:10.5px}
.news li{position:relative;padding-left:8px;margin-bottom:14px}
.news li::before{content:"";position:absolute;left:0;top:4px;width:3px;height:3px;border-radius:50%;background:#c9962a}
.foot-brand{left:106px;top:1085px}
.foot-brand .brand-dot{width:34px;height:34px}
.foot-brand .brand-name{font-size:32px;color:var(--gold)}
.testimonial{left:330px;top:1030px;width:185px;color:var(--white)}
.testimonial h3{font-family:"Marcellus",serif;font-weight:400;font-size:21px}
.testimonial p{font-size:10px;line-height:14.5px;margin-top:12px;padding-left:3px}
.testimonial .who{font-style:italic;font-weight:600;font-size:9px;margin-top:10px;padding-left:3px}
.badges{left:600px;top:1026px;width:152px;display:flex;flex-wrap:wrap;justify-content:center;gap:8px 14px}
.badges span{width:34px;height:26px;background:#e6e6e6;border-radius:3px}
.contact{left:436px;top:1110px;width:320px;text-align:right;font-family:Arial,sans-serif;font-size:8.5px;line-height:13.5px;color:var(--white);white-space:nowrap}
</style>
</head>
<body>
<div class="canvas">
  <div class="page">
    <div class="abs brand header-brand"><span class="brand-dot"></span><span class="brand-name">Stoneridge</span></div>

    <div class="abs offices">
      <address style="font-style:normal"><b>Main Office:</b><br>417 E Hazel Rd<br>Marston, VA 24873<br>(800) 555-0173 &middot; (540) 555-0148</address>
      <address style="font-style:normal"><b>Dunmore Office:</b><br>318 1/2 S. Mill Rd.<br>Dunmore, WV 24987<br>(304) 555-0161</address>
    </div>

    <div class="abs social"><span></span><span></span><span></span></div>

    <nav class="abs nav">
      <a>HOME</a><a class="wide">REAL ESTATE</a><a class="wide">AUCTION CALENDAR</a><a>ABOUT US</a><a class="wide">TERMS &amp; CONDITIONS</a><a>FAQ</a><a class="wide">CONTACT US</a>
    </nav>

    <div class="abs slider" role="img" aria-label="Stock photo of a suburban house at dusk with an auction sign in the yard"></div>
    <div class="abs dots"><span></span><span class="on"></span><span></span><span></span></div>

    <section class="abs signup">
      <h3>Email Signup</h3>
      <p>Please join our free mailing list to get auction alerts for upcoming events.</p>
      <div class="field">Enter Your Email</div>
      <span class="btn">Subscribe</span>
    </section>

    <div class="abs dropdown">
      <div class="d1">Current Auctions</div>
      <div class="d2">Past Auctions</div>
    </div>

    <section class="abs welcome">
      <h1>Welcome to STONERIDGE</h1>
      <p>Since 1977, we at R. Whitfield and Associates, Inc., the premier auction firm in the South, dedicate ourselves to providing our clients with professional, high-quality services to meet all our clients' auction needs. When you partner with R. Whitfield.</p>
    </section>

    <article class="abs listing" style="top:458px">
      <h2>2280 BIRCHWOOD LANE, ALTON, GA</h2>
      <div class="body">
        <div class="photo" role="img" aria-label="Photo of a two-storey house with a front porch"></div>
        <div class="info">
          <h4>Thursday, August 21st at 10:00 A.M.</h4>
          <p class="sell">Selling 3120 Acres of land in tracts of 2590<br>Acres&amp; 560 Acres</p>
          <p style="margin-top:8px"><b>LIVE OFF-SITE AUCTION</b></p>
          <p><b>Auction Location:</b></p>
          <p class="pinrow"><svg width="8" height="10" viewBox="0 0 8 10"><path d="M4 0a4 4 0 0 1 4 4c0 3-4 6-4 6S0 7 0 4a4 4 0 0 1 4-4z" fill="var(--pin)"/></svg>508 N Main St, Elmwood, OK 73801</p>
          <p><b>Property Location:</b></p>
          <p class="pinrow"><svg width="8" height="10" viewBox="0 0 8 10"><path d="M4 0a4 4 0 0 1 4 4c0 3-4 6-4 6S0 7 0 4a4 4 0 0 1 4-4z" fill="var(--pin)"/></svg>508 N Main St, Elmwood, OK 73801</p>
          <p><b>Begins:</b>&nbsp;&nbsp; 08/21/14 at 10:00 AM CDT</p>
        </div>
        <div class="btns"><span><i></i>Details</span><span><i></i>Photos</span></div>
      </div>
    </article>

    <article class="abs listing" style="top:693px">
      <h2>2280 BIRCHWOOD LANE, ALTON, GA</h2>
      <div class="body">
        <div class="photo" role="img" aria-label="Photo of a two-storey house with a front porch"></div>
        <div class="info">
          <h4>Thursday, August 21st at 10:00 A.M.</h4>
          <p class="sell">Selling 3120 Acres of land in tracts of 2590<br>Acres&amp; 560 Acres</p>
          <p style="margin-top:8px"><b>LIVE OFF-SITE AUCTION</b></p>
          <p><b>Auction Location:</b></p>
          <p class="pinrow"><svg width="8" height="10" viewBox="0 0 8 10"><path d="M4 0a4 4 0 0 1 4 4c0 3-4 6-4 6S0 7 0 4a4 4 0 0 1 4-4z" fill="var(--pin)"/></svg>508 N Main St, Elmwood, OK 73801</p>
          <p><b>Property Location:</b></p>
          <p class="pinrow"><svg width="8" height="10" viewBox="0 0 8 10"><path d="M4 0a4 4 0 0 1 4 4c0 3-4 6-4 6S0 7 0 4a4 4 0 0 1 4-4z" fill="var(--pin)"/></svg>508 N Main St, Elmwood, OK 73801</p>
          <p><b>Begins:</b>&nbsp;&nbsp; 08/21/14 at 10:00 AM CDT</p>
        </div>
        <div class="btns"><span><i></i>Details</span><span><i></i>Photos</span></div>
      </div>
    </article>

    <div class="abs video" role="img" aria-label="Video still of an outdoor auction with an auctioneer and crowd">
      <div class="abs play"><svg width="48" height="48" viewBox="0 0 48 48"><path d="M19 14l16 10-16 10z" fill="#fff"/></svg></div>
      <div class="abs vbar"><div class="abs vtrack"></div></div>
    </div>

    <section class="abs widget featured">
      <h3>Featured Auctions</h3>
      <p class="t">13.35 ACRES OF PRIME DEVELOP<br>&amp; 33RD STREET</p>
      <div class="img" role="img" aria-label="Photo of a crowd gathered outside a farmhouse"></div>
      <p class="b">LOTS 13 &amp; 14 FOR SALE, PINECREST<br>IOWA<br>Third Street, Pinecrest, IA 52600</p>
    </section>

    <section class="abs widget news">
      <h3>News &amp; Events Blog</h3>
      <ul>
        <li>Great Land Auction Companies Make All the Difference</li>
        <li>Great OK Farms for Sale at Auction Prices</li>
        <li>Farmland Auctions on Route 66</li>
        <li>Great Land Auction Companies Make All the Difference</li>
        <li>Great OK Farms for Sale at Auction Prices</li>
      </ul>
    </section>
  </div>

  <div class="abs brand foot-brand"><span class="brand-dot"></span><span class="brand-name">Stoneridge</span></div>

  <section class="abs testimonial">
    <h3>Testimonial</h3>
    <p>&#8220; Using R. Whitfield &amp; Associates to take listings from "old" to "sold" is a win-win experience that I recommend to other brokers in need of assistance in marketing their Stale Listings. &#8221;</p>
    <p class="who">..Mel Harrow</p>
  </section>

  <div class="abs badges"><span></span><span></span><span></span><span></span><span></span><span></span></div>

  <div class="abs contact">
    Stoneridge Real Esate &amp; Auction, LLC / Alan Prescott<br>
    email: stoneridge@mailbox.com; alan.prescott@hearthrealty.com<br>
    phone: (859) 555-0192 mobile phone: (859) 555-0127<br>
    Copyright &copy; 2014: Stoneridge Real Estate Auction. LLC
  </div>
</div>
</body>
</html>
```